Business cards for a new business: Willow Brook Calm Healing

I would like for the card to include a lotus. The business is a healing practice so I'd like the overall colours to be pink and green and for it to have a soft feel. The name of the practice is
"Willow Brook Calm Healing", which I'd like to be included, as well as the words: "Energetic and spiritual healing to restore health, harmony and wellbeing". Also, my name - Tarik and the number: 5391 6048

Target Market(s)

Everyone interested in personal healing!

Industry/Entity Type

Business

Contact Information for Business Card

As above……..could be single or double-sided
I'd like the font for the name of the practice and my name to be in green and be a flowing, but simple font - elegant.
The background to be a light pink. See below for colours

Colors
f9d9e8
eea4c8
e567a6
d0ebe7
86cfc6
33b7a4

Requirements
Must have
• See above
Nice to have
• See above

```html
<!DOCTYPE html>
<html lang="en">
<head>
<meta charset="utf-8">
<title>Willow Brook Calm Healing – Business Cards</title>
<link href="https://fonts.googleapis.com/css2?family=Cabin:wght@400;600;700&family=Dancing+Script:wght@500&display=swap" rel="stylesheet">
<style>
  :root {
    --blush: #f9d9e8;
    --rose: #eea4c8;
    --fuchsia: #e567a6;
    --mist: #d0ebe7;
    --aqua: #86cfc6;
    --teal: #33b7a4;
    --white: #ffffff;
    --stage-light: #7b7b7b;
    --stage-dark: #4e4e4e;
  }
  * { box-sizing: border-box; margin: 0; padding: 0; }
  html, body { width: 1200px; height: 961px; overflow: hidden; }
  body {
    position: relative;
    background: radial-gradient(ellipse at 50% 40%, var(--stage-light) 0%, #666 45%, var(--stage-dark) 100%);
    font-family: "Cabin", Arial, sans-serif;
    color: var(--white);
  }
  .card {
    position: absolute;
    overflow: hidden;
    box-shadow: 0 4px 10px rgba(0,0,0,0.35);
    text-align: center;
  }
  .card--landscape {
    width: 370px; height: 211px;
    border-radius: 40px 0 40px 0;
  }
  .card--portrait { width: 222px; height: 391px; }
  .card--pink-wave { left: 124px; top: 249px; background: linear-gradient(100deg, #f4bcd8 0%, var(--rose) 55%, #ea93c1 100%); }
  .card--teal-wave { left: 124px; top: 519px; background: linear-gradient(100deg, #3cbba9 0%, var(--teal) 100%); }
  .card--aqua-lotus { left: 596px; top: 338px; background: var(--aqua); }
  .card--fuchsia-lotus { left: 903px; top: 338px; background: var(--fuchsia); }

  .waves { position: absolute; inset: 0; width: 100%; height: 100%; }

  .practice-name {
    position: absolute;
    font-family: "Dancing Script", cursive;
    font-weight: 500;
    color: var(--white);
    line-height: 1;
  }
  .practice-name span { display: block; }
  .practice-name .name-sub { text-align: right; }
  .card--landscape .practice-name { left: 30px; top: 32px; width: 228px; font-size: 38px; }
  .card--landscape .name-sub { font-size: 24px; margin-top: 2px; }
  .card--portrait .practice-name { left: 18px; top: 62px; width: 184px; font-size: 32px; }
  .card--portrait .name-sub { font-size: 22px; margin-top: 2px; }

  .flower-mark {
    position: absolute;
    left: 258px; top: 8px; width: 82px; height: 100px;
    border-radius: 45% 45% 40% 40%;
    background: radial-gradient(ellipse at 50% 55%, rgba(255,255,255,0.4) 0%, rgba(255,255,255,0.12) 55%, rgba(255,255,255,0) 75%);
  }
  .card--teal-wave .flower-mark { left: 240px; top: 4px; width: 110px; height: 120px; }
  .lotus-art {
    position: absolute;
    left: -10px; top: 200px; width: 175px; height: 150px;
    border-radius: 50% 50% 20% 20% / 70% 70% 30% 30%;
    background: radial-gradient(ellipse at 50% 65%, rgba(255,255,255,0.34) 0%, rgba(255,255,255,0.2) 50%, rgba(255,255,255,0) 78%);
  }

  .owner { position: absolute; left: 0; width: 100%; font-weight: 700; font-size: 19px; line-height: 1; }
  .phone { position: absolute; left: 0; width: 100%; font-size: 13px; line-height: 1; }
  .tagline { position: absolute; left: 0; width: 100%; font-size: 9.5px; line-height: 13px; font-weight: 600; }

  .card--landscape .owner { top: 134px; }
  .card--landscape .phone { top: 155px; }
  .card--landscape .tagline { top: 171px; }
  .card--portrait .owner { top: 164px; }
  .card--portrait .phone { top: 186px; }
  .card--portrait .tagline { top: 349px; font-size: 8.5px; line-height: 11px; }
</style>
</head>
<body>

  <article class="card card--landscape card--pink-wave">
    <svg class="waves" viewBox="0 0 370 211" preserveAspectRatio="none" aria-hidden="true">
      <path d="M0 90 C90 50 170 60 240 85 C300 105 340 95 370 80 L370 110 C330 125 290 118 230 100 C160 80 90 85 0 125 Z" fill="rgba(255,255,255,0.22)"/>
      <path d="M0 140 C100 90 200 100 270 120 C320 135 350 130 370 120 L370 211 L0 211 Z" fill="rgba(255,255,255,0.12)"/>
      <path d="M0 112 C80 78 160 80 230 96 C290 110 340 104 370 94" stroke="rgba(255,255,255,0.5)" stroke-width="1.5" fill="none"/>
    </svg>
    <div class="flower-mark" role="img" aria-label="Line drawing of a lotus flower"></div>
    <h1 class="practice-name"><span>Willow Brook</span><span class="name-sub">Calm Healing</span></h1>
    <p class="owner">Tarik</p>
    <p class="phone">5391 6048</p>
    <p class="tagline">|Energetic and spiritual healing to restore health|<br>| harmony and wellbeing |</p>
  </article>

  <article class="card card--landscape card--teal-wave">
    <svg class="waves" viewBox="0 0 370 211" preserveAspectRatio="none" aria-hidden="true">
      <path d="M0 95 C90 55 170 62 240 86 C300 106 340 96 370 82 L370 112 C330 126 290 120 230 102 C160 82 90 88 0 130 Z" fill="rgba(255,255,255,0.2)"/>
      <path d="M0 145 C100 95 200 104 270 124 C320 138 350 133 370 123 L370 211 L0 211 Z" fill="rgba(255,255,255,0.1)"/>
      <path d="M0 116 C80 80 160 82 230 98 C290 112 340 106 370 96" stroke="rgba(255,255,255,0.45)" stroke-width="1.5" fill="none"/>
    </svg>
    <div class="flower-mark" role="img" aria-label="Line drawing of a lotus flower over faint lotus petals"></div>
    <h1 class="practice-name"><span>Willow Brook</span><span class="name-sub">Calm Healing</span></h1>
    <p class="owner">Tarik</p>
    <p class="phone">5391 6048</p>
    <p class="tagline">|Energetic and spiritual healing to restore health|<br>| harmony and wellbeing |</p>
  </article>

  <article class="card card--portrait card--aqua-lotus">
    <h1 class="practice-name"><span>Willow Brook</span><span class="name-sub">Calm Healing</span></h1>
    <p class="owner">Tarik</p>
    <p class="phone">5391 6048</p>
    <div class="lotus-art" role="img" aria-label="Large faint translucent lotus flower"></div>
    <p class="tagline">|Energetic and spiritual healing to restore health|<br>| harmony and wellbeing |</p>
  </article>

  <article class="card card--portrait card--fuchsia-lotus">
    <h1 class="practice-name"><span>Willow Brook</span><span class="name-sub">Calm Healing</span></h1>
    <p class="owner">Tarik</p>
    <p class="phone">5391 6048</p>
    <div class="lotus-art" role="img" aria-label="Large faint translucent lotus flower"></div>
    <p class="tagline">|Energetic and spiritual healing to restore health|<br>| harmony and wellbeing |</p>
  </article>

</body>
</html>
```